Cedar Hall businesscard

We changed our name and logo, now we need new business cards.
3-4/72 Marlow Street Elmvale 2761
www.cedarhall-example.org.au
info@cedarhall-example.org.au
Lorna-Jean Whitcombe
Senior Pastor
ph: 02 95874210

```html
<!DOCTYPE html>
<html lang="en">
<head>
<meta charset="utf-8">
<title>Cedar Hall – Business Card</title>
<link href="https://fonts.googleapis.com/css2?family=Lato:wght@300;400;700;900&display=swap" rel="stylesheet">
<style>
  :root {
    --backdrop: #e6e4e1;
    --card-white: #ffffff;
    --slate: #5f7184;
    --slate-deep: #4a6580;
    --slate-light: #a7b8c8;
    --ink-light: #ffffff;
  }
  * { margin: 0; padding: 0; box-sizing: border-box; }
  html, body {
    width: 1200px;
    height: 900px;
    overflow: hidden;
    background: var(--backdrop);
    font-family: "Lato", sans-serif;
  }
  .business-card {
    position: absolute;
    left: 100px;
    top: 164px;
    width: 1000px;
    height: 572px;
    background: var(--slate);
    overflow: hidden;
    box-shadow: 0 18px 40px rgba(0,0,0,0.25);
  }
  .card-shapes {
    position: absolute;
    inset: 0;
  }
  .brand-name {
    position: absolute;
    left: 50px;
    top: 252px;
    width: 420px;
    display: flex;
    align-items: center;
    justify-content: center;
    gap: 16px;
    color: var(--slate);
    font-weight: 300;
    font-size: 50px;
    letter-spacing: 3px;
    text-transform: uppercase;
  }
  .brand-dot {
    width: 20px;
    height: 20px;
    border-radius: 50%;
    background: var(--slate);
    flex: none;
  }
  .card-details {
    position: absolute;
    left: 572px;
    top: 62px;
    width: 400px;
    color: var(--ink-light);
  }
  .person-name {
    font-weight: 900;
    font-size: 29px;
    letter-spacing: 0.3px;
    white-space: nowrap;
  }
  .person-role {
    font-weight: 700;
    font-size: 20px;
    margin-top: 2px;
    padding-left: 12px;
  }
  .postal-address {
    font-style: normal;
    font-weight: 700;
    font-size: 21px;
    line-height: 1.3;
    margin-top: 44px;
    padding-left: 40px;
  }
  .contact-list {
    list-style: none;
    margin-top: 30px;
    padding-left: 62px;
    font-weight: 700;
    font-size: 20px;
    line-height: 1.6;
  }
  .contact-list li {
    display: flex;
    align-items: center;
    gap: 8px;
    white-space: nowrap;
  }
  .contact-icon {
    width: 18px;
    height: 18px;
    flex: none;
  }
</style>
</head>
<body>
  <div class="business-card">
    <svg class="card-shapes" width="1000" height="572" viewBox="0 0 1000 572" aria-hidden="true">
      <circle class="curve-deep" cx="150" cy="310" r="450" fill="var(--slate-deep)"/>
      <circle class="curve-light" cx="145" cy="305" r="427" fill="var(--slate-light)"/>
      <circle class="curve-white" cx="140" cy="300" r="404" fill="var(--card-white)"/>
    </svg>

    <div class="brand-name">
      <span class="brand-dot"></span>
      <span>Cedar Hall</span>
    </div>

    <div class="card-details">
      <div class="person-name">Lorna-Jean Whitcombe</div>
      <div class="person-role">Senior Pastor</div>

      <address class="postal-address">
        3-4/72 Marlow Street<br>
        Elmvale 2761
      </address>

      <ul class="contact-list">
        <li>
          <svg class="contact-icon" viewBox="0 0 24 24" aria-hidden="true">
            <path fill="#fff" d="M6.6 10.8a15.1 15.1 0 0 0 6.6 6.6l2.2-2.2a1 1 0 0 1 1-.25 11.4 11.4 0 0 0 3.6.57 1 1 0 0 1 1 1V20a1 1 0 0 1-1 1A17 17 0 0 1 3 4a1 1 0 0 1 1-1h3.5a1 1 0 0 1 1 1c0 1.25.2 2.45.57 3.6a1 1 0 0 1-.25 1z"/>
          </svg>
          <span>02 95874210</span>
        </li>
        <li>
          <svg class="contact-icon" viewBox="0 0 24 24" aria-hidden="true">
            <rect x="2" y="5" width="20" height="14" rx="1.5" fill="#fff"/>
            <path d="M2.5 6l9.5 7 9.5-7" fill="none" stroke="var(--slate)" stroke-width="1.6"/>
          </svg>
          <span>info@cedarhall-example.org.au</span>
        </li>
        <li>
          <svg class="contact-icon" viewBox="0 0 24 24" aria-hidden="true">
            <g fill="none" stroke="#fff" stroke-width="1.6">
              <circle cx="12" cy="12" r="9"/>
              <ellipse cx="12" cy="12" rx="4" ry="9"/>
              <path d="M3 12h18M4.5 7.5h15M4.5 16.5h15"/>
            </g>
          </svg>
          <span>www.cedarhall-example.org.au</span>
        </li>
      </ul>
    </div>
  </div>
</body>
</html>
```